8x8 Social Media Ad - Harbor Summit Expo

Attention Real Estate Agents
Please join us for our
Quarterly Real Estate Training Expo
The 2nd Saturday of February, May, August and November
Our Next Training Expo is _________________________________
From 9 am to 1 pm
at
Marlowe Suites Fernridge Station
4187 Copperleaf Lane, Greenbelt, MD 20770
Scheduled Speakers
9:00 am - Desmond Pryce - Orientation
9:30 am - Terrell Oakes - Multiple Income Streams / Keystone Track
10:00 am - Lorna Beckett - Marketing though Social Media
10:45 am - Raul Denning - Generating Business through Kelp-Nest
11:30 am - Tunde Adesemi - Real Estate Investing
12:15 pm - Marcus Oyelowo - (Main Speaker) Training Topic TBA
For more information call Desmond Pryce at (240) 555-0192 or email dpryce@harborsummithomes.example

```html
<!DOCTYPE html>
<html lang="en">
<head>
<meta charset="utf-8">
<title>Harbor Summit Expo – Quarterly Real Estate Training Expo</title>
<link href="https://fonts.googleapis.com/css2?family=Montserrat:wght@400;500;600;700;800;900&display=swap" rel="stylesheet">
<style>
  :root {
    --teal: #0b7d82;
    --teal-deep: #0d5c61;
    --ink: #2a2a33;
    --night: #0a1416;
    --paper: #ececee;
    --white: #ffffff;
  }
  html, body { margin: 0; padding: 0; overflow: hidden; background: var(--paper); }
  .ad { width: 1200px; height: 1200px; display: block; font-family: "Montserrat", sans-serif; }
  .headline { font-weight: 900; fill: var(--white); }
  .subhead { font-weight: 700; fill: var(--white); }
  .expo-title { font-weight: 600; fill: var(--teal); }
  .band-text { font-weight: 500; fill: var(--white); }
  .band-strong { font-weight: 700; fill: var(--white); }
  .section-title { font-weight: 800; fill: var(--white); }
  .slot-time { font-weight: 700; fill: var(--teal); }
  .slot-name { font-weight: 700; fill: var(--ink); }
  .slot-topic { font-weight: 400; fill: var(--ink); }
  .contact-lead { font-weight: 600; fill: var(--teal); }
  .contact-phone { font-weight: 700; fill: var(--ink); }
  .contact-email { font-weight: 500; fill: var(--ink); }
  .brand-name { font-weight: 800; fill: var(--teal); }
  .speaker-photo { stroke: var(--teal); stroke-width: 2; }
</style>
</head>
<body>
<svg class="ad" viewBox="0 0 1200 1200" xmlns="http://www.w3.org/2000/svg">
  <defs>
    <linearGradient id="sceneTone" x1="0" y1="0" x2="1" y2="1">
      <stop offset="0" stop-color="#2c4447"/>
      <stop offset="0.45" stop-color="#10282b"/>
      <stop offset="1" stop-color="#050c0d"/>
    </linearGradient>
    <linearGradient id="venueBand" x1="0" y1="0" x2="1" y2="0">
      <stop offset="0" stop-color="#061214"/>
      <stop offset="0.35" stop-color="#0b3f43"/>
      <stop offset="1" stop-color="var(--teal)"/>
    </linearGradient>
    <linearGradient id="portraitTone" x1="0" y1="0" x2="0" y2="1">
      <stop offset="0" stop-color="#a9aeb2"/>
      <stop offset="1" stop-color="#3b3f45"/>
    </linearGradient>
  </defs>

  <!-- backdrop -->
  <rect class="backdrop-scene" x="0" y="0" width="1200" height="801" fill="url(#sceneTone)" role="img" aria-label="Modern white house with pool at dusk, in dark teal tones"/>
  <rect x="0" y="801" width="1200" height="399" fill="var(--paper)"/>

  <!-- header panel -->
  <path d="M113 0 H1056 V242 Q1056 329 969 329 H200 Q113 329 113 242 Z" fill="var(--teal)" opacity="0.88"/>
  <line x1="186" y1="154" x2="1056" y2="154" stroke="var(--white)" stroke-width="2"/>

  <g class="brand-badge">
    <circle cx="118" cy="114" r="80" fill="var(--white)" stroke="var(--teal)" stroke-width="5"/>
    <text class="brand-name" x="118" y="108" font-size="17" text-anchor="middle">Harbor Summit</text>
    <text class="brand-name" x="118" y="130" font-size="17" text-anchor="middle">Homes</text>
  </g>

  <text class="headline" x="602" y="134" font-size="98" text-anchor="middle" letter-spacing="2">ATTENTION</text>
  <text class="subhead" x="600" y="224" font-size="58" text-anchor="middle">REAL ESTATE AGENTS</text>
  <text class="subhead" x="586" y="273" font-size="27" text-anchor="middle">PLEASE JOIN US FOR OUR</text>

  <rect x="307" y="300" width="559" height="60" rx="5" fill="var(--white)"/>
  <text class="expo-title" x="587" y="339" font-size="27" text-anchor="middle">Quarterly Real Estate Training Expo</text>

  <!-- schedule band -->
  <polygon points="0,373 755,373 699,472 0,472" fill="var(--teal)" stroke="var(--white)" stroke-width="4"/>
  <text class="band-text" x="45" y="413" font-size="20.5">The 2nd Saturday of February, May, August and November</text>
  <text class="band-text" x="45" y="446" font-size="20.5">Our Next Training Expo is</text>
  <line x1="340" y1="444" x2="681" y2="444" stroke="var(--white)" stroke-width="1.5" stroke-dasharray="9 4"/>

  <!-- venue band -->
  <polygon points="410,484 1204,482 1204,612 466,605" fill="url(#venueBand)" stroke="var(--white)" stroke-width="4"/>
  <text class="band-strong" x="492" y="521" font-size="21">From 9 am to 1 pm at</text>
  <text class="band-text" x="492" y="554" font-size="21">Marlowe Suites Fernridge Station</text>
  <text class="band-text" x="492" y="587" font-size="21">4187 Copperleaf Lane, Greenbelt, MD 20770</text>

  <text class="section-title" x="589" y="676" font-size="36" text-anchor="middle">SCHEDULED SPEAKERS</text>

  <!-- speaker photos -->
  <rect class="speaker-photo" x="57" y="725" width="202" height="138" rx="9" fill="url(#portraitTone)" role="img" aria-label="Portrait of Desmond Pryce"/>
  <rect class="speaker-photo" x="278" y="725" width="199" height="138" rx="9" fill="#16252a" role="img" aria-label="Promotional portrait of Terrell Oakes"/>
  <rect class="speaker-photo" x="499" y="727" width="200" height="137" rx="9" fill="#6b6d72" role="img" aria-label="Portrait of Lorna Beckett"/>
  <rect class="speaker-photo" x="721" y="727" width="198" height="135" rx="9" fill="#2a2725" role="img" aria-label="Portrait of Raul Denning and colleague"/>
  <rect class="speaker-photo" x="942" y="728" width="200" height="135" rx="9" fill="#5f7a4e" role="img" aria-label="Outdoor portrait of Tunde Adesemi"/>

  <!-- speaker slots -->
  <g font-size="20" text-anchor="middle">
    <text class="slot-time" x="155" y="899" font-size="21">9:00 am</text>
    <text class="slot-name" x="158" y="932" font-size="21">Desmond Pryce</text>
    <text class="slot-topic" x="155" y="964">Orientation</text>

    <text class="slot-time" x="381" y="899" font-size="21">9:30 am</text>
    <text class="slot-name" x="384" y="932" font-size="21">Terrell Oakes</text>
    <text class="slot-topic" x="382" y="964">Multiple Income</text>
    <text class="slot-topic" x="382" y="997">Streams / Keystone</text>
    <text class="slot-topic" x="382" y="1031">Track</text>

    <text class="slot-time" x="609" y="899" font-size="21">10:00 am</text>
    <text class="slot-name" x="609" y="932" font-size="21">Lorna Beckett</text>
    <text class="slot-topic" x="609" y="964">Marketing though</text>
    <text class="slot-topic" x="609" y="997">Social Media</text>

    <text class="slot-time" x="832" y="899" font-size="21">10:45 am</text>
    <text class="slot-name" x="832" y="932" font-size="21">Raul Denning</text>
    <text class="slot-topic" x="832" y="964">Generating Business</text>
    <text class="slot-topic" x="832" y="997">through Kelp-Nest</text>

    <text class="slot-time" x="1045" y="899" font-size="21">11:30 am</text>
    <text class="slot-name" x="1045" y="932" font-size="21">Tunde Adesemi</text>
    <text class="slot-topic" x="1045" y="964">Real Estate</text>
    <text class="slot-topic" x="1045" y="997">Investing</text>
  </g>

  <!-- main speaker -->
  <rect class="speaker-photo" x="53" y="1031" width="200" height="135" rx="9" fill="#4a4f55" role="img" aria-label="Portrait of main speaker Marcus Oyelowo"/>
  <text class="slot-time" x="277" y="1079" font-size="21">12:15 pm</text>
  <text class="slot-name" x="277" y="1112" font-size="21">Marcus Oyelowo</text>
  <text class="slot-topic" x="277" y="1146" font-size="20">(Main Speaker) Training Topic TBA</text>

  <!-- contact -->
  <text class="contact-lead" x="748" y="1067" font-size="22">For more information call</text>
  <text class="contact-lead" x="748" y="1094" font-size="22">Desmond Pryce at</text>
  <g class="phone-icon">
    <circle cx="776" cy="1145" r="31" fill="var(--teal)"/>
    <path d="M765 1128 c3 -2 6 -1 7 2 l3 7 c1 3 0 5 -2 6 l-3 2 c2 5 6 9 11 11 l2 -3 c1 -2 3 -3 6 -2 l7 3 c3 1 4 4 2 7 l-3 4 c-3 3 -8 3 -13 1 c-11 -5 -19 -13 -23 -24 c-2 -5 -1 -10 2 -13 z" fill="var(--white)"/>
  </g>
  <text class="contact-phone" x="823" y="1142" font-size="34">(240) 555-0192</text>
  <text class="contact-email" x="823" y="1171" font-size="17">dpryce@harborsummithomes.example</text>
</svg>
</body>
</html>
```